Business Card & Logo Design - Hedge Fund

We need a business card and logo design for a hedge fund. The hedge fund is named Morvane Equity LLC. Morvane Equity was created by finance professors and the strategy is based academic research that looks for patterns in stock prices. The design should look conservative, solid, strong. We favor a classic style - nothing flashy. The logo can relate to the name Morvane Equity, or it could involve a symbol design that connotes "science" . We are open to ideas. We do not want alot of colors - but if any, color - blue is preferred. The font that seems to look best for the name (Morvane Equity) is arial black. We are open to ideas. Most important - we want to see a mock up of an actual business card with the logo concept embedded. The business card should include space for : company name, individual name, position title, cell phone, address. We hope to have this work done by Sept. 8.

Target Market(s)

We will be meeting with and giving the business card to institutions and high net worth individuals.

Industry/Entity Type

Investment Advisory

Contact Information for Business Card

Company name - Morvane Equity LLC
Individual name - Peter Dalby
Title - Portfolio Manager
Cell - (412) 555-0187
Address - 2650 Birchmont Lane, Suite 300, Atlanta GA 30327

Font styles to use
Other font styles liked:
• Arial

Colors
3277b5
0255a3
85acd3
cedeed
fdf9cf
d9d9d9
e6e6e6
f04a50
6b449b

Requirements
Must have
• Must have card details that are sited above.
• We would like a logo related to the name (Morvane Equity) or concept of the fund.
Nice to have
• We want conservative / understated / clean crisp look.
• If any colors - we prefer conservative appearance - blue / gray.
• I have enclosed an example of a card style that looks attractive - please do not exactly copy this card. This is not our company or logo. I feel the layout is attractive - just as an example
Should not have
• Avoid too much color.
• I have selected some preferred colors. Please do not use all of the colors - I have selected a few that might work - but I am not sure. We are open to your ideas so please do not feel the need to use all or any of these.

```html
<!DOCTYPE html>
<html lang="en">
<head>
<meta charset="utf-8">
<title>Morvane Equity LLC – Business Card</title>
<link rel="stylesheet" href="https://fonts.googleapis.com/css2?family=Arimo:wght@400;700&display=swap">
<style>
  :root {
    --card-white: #ffffff;
    --panel-gray: #808080;
    --stripe-gray: #b4b5b7;
    --brand-gray: #7f7f7f;
    --text-light: #ffffff;
  }
  html, body {
    margin: 0;
    padding: 0;
    overflow: hidden;
    background: var(--card-white);
  }
  .card {
    position: relative;
    width: 1200px;
    height: 762px;
    overflow: hidden;
    background: var(--card-white);
    font-family: "Arimo", Arial, sans-serif;
  }
  .card__backdrop {
    position: absolute;
    inset: 0;
  }
  .brand {
    position: absolute;
    left: 28px;
    top: 186px;
    width: 520px;
    text-align: center;
  }
  .brand__square {
    display: block;
    width: 160px;
    height: 160px;
    margin: 0 auto;
    background: var(--brand-gray);
  }
  .brand__name {
    margin: 20px 0 0;
    font-weight: 700;
    font-size: 45px;
    line-height: 1;
    letter-spacing: 1px;
    color: var(--brand-gray);
    white-space: nowrap;
  }
  .contact {
    position: absolute;
    margin: 0;
    text-align: center;
    color: var(--text-light);
    font-weight: 400;
    white-space: nowrap;
    line-height: 1;
  }
  .contact__name {
    top: 260px;
    left: 664px;
    width: 560px;
    font-size: 84px;
  }
  .contact__title {
    top: 344px;
    left: 666px;
    width: 560px;
    font-size: 54px;
  }
  .contact__phone {
    top: 438px;
    left: 666px;
    width: 540px;
    font-size: 54px;
  }
  .contact__address {
    top: 551px;
    left: 636px;
    width: 560px;
    font-size: 55px;
    font-style: normal;
    line-height: 64px;
  }
</style>
</head>
<body>
  <div class="card">
    <svg class="card__backdrop" width="1200" height="762" viewBox="0 0 1200 762" aria-hidden="true">
      <polygon class="card__stripe" points="766,0 1200,0 1200,762 475,762" fill="var(--stripe-gray)"/>
      <polygon class="card__panel" points="795,0 1200,0 1200,762 505,762" fill="var(--panel-gray)"/>
    </svg>

    <div class="brand">
      <span class="brand__square" aria-hidden="true"></span>
      <p class="brand__name">Morvane Equity LLC</p>
    </div>

    <h1 class="contact contact__name">Peter Dalby</h1>
    <h2 class="contact contact__title">Portfolio Manager</h2>
    <div class="contact contact__phone">(412) 555-0187</div>
    <address class="contact contact__address">
      2650 Birchmont Lane,<br>
      Suite 300, Atlanta<br>
      GA 30327
    </address>
  </div>
</body>
</html>
```